CareWillow Brand Standards and Core Values

I would like to have frameable posters made up for each office using our brand standards. I would like the posters to include:Our Vision Statement:We are transforming the healthcare staffing and homecare industry with our people-oriented, world-class team. Clients choose us, and develop lasting bonds with our team because of our impeccably high standards and our reputation for always remembering this is, first and foremost, a people business. We consistently go the extra mile to ensure our nurses and those being cared for are at all times, treated with dignity and respect. We hold ourselves and those we work with to the highest possible standards. We consistently deliver what we promise, and whenever possible, even more. Our Mission Statement:We go above and beyond to ensure our clients receive the right care and the right people at the right time. Our rigorous recruitment standards result in strong caregivers who are trusted for their expertise, experience and compassion. Our Values:Through our genuine caring and compassion, we are committed to honor all with whom we interact. We are grounded in our faith and dedicated to working together as a family that consistently and passionately lives our values. Compassion Integrity and honesty Faith Decisive action Constant and never-ending improvement Personal ownership Excellence Positive attitude Passion RespectWho we are:We are friendly, servant leaders who have a sense of urgency to meet the needs of our nurses and clients. We prioritize personal relationships with genuine caring and compassion. We inspire others through our passion and energy.Our main colors are: HEX# 5C80DE, HEX# BDE080, HEX# 8C8C8Caccent colors are: HEX# 95D6E3, HEX# AD59AB, HEX# 002E57

Target Market(s)

office employee inspiration

Font styles to use
Other font styles liked:
• Verdana

Colors

Designer to choose colors to be used in the design.

Requirements
Must have
• the core values listed in description
Nice to have
• colors given in description, something fun and inspiring for office employees to help motivate them !
Should not have
• colors that are not company colors. I have listed HEX codes in description

```html
<!DOCTYPE html>
<html lang="en">
<head>
<meta charset="utf-8">
<title>CareWillow – Brand Standards &amp; Core Values</title>
<link rel="stylesheet" href="https://fonts.googleapis.com/css2?family=Arimo:wght@400;700&display=swap">
<style>
  :root {
    --brand-blue: #5C80DE;
    --ribbon-blue: #6A82C4;
    --ribbon-fold: #4A5F99;
    --brand-green: #BDE080;
    --brand-grey: #8C8C8C;
    --text-dark: #3E3E3E;
    --header-bg: #F4F4F4;
    --paper: #FFFFFF;
  }
  * { box-sizing: border-box; margin: 0; padding: 0; }
  html, body { width: 1005px; height: 1200px; overflow: hidden; background: var(--paper); }
  body { font-family: "Arimo", Arial, sans-serif; color: var(--text-dark); position: relative; }

  .poster { position: absolute; inset: 0; background: var(--paper); }

  .header-bar {
    position: absolute; left: 0; top: 0; width: 1005px; height: 64px;
    background: var(--header-bg); border-bottom: 4px solid var(--brand-green);
  }
  .header-title {
    position: absolute; right: 28px; top: 20px;
    font-size: 23px; color: var(--brand-blue); letter-spacing: 0.3px;
  }

  .hero-photo {
    position: absolute; left: 0; top: 76px; width: 1005px; height: 436px;
    background: linear-gradient(100deg, #7E9A5C 0%, #B9C79A 35%, #D9D2C4 55%, #9FB3C9 80%, #C7D3E0 100%);
  }

  .logo-panel { position: absolute; left: 29px; top: 0; width: 334px; height: 230px; }
  .logo-panel svg { position: absolute; inset: 0; filter: drop-shadow(0 2px 3px rgba(0,0,0,.15)); }
  .logo-mark {
    position: absolute; left: 0; width: 334px; top: 120px; text-align: center;
    font-size: 38px; color: var(--brand-grey); font-weight: 400;
  }
  .logo-dot {
    position: absolute; left: 145px; top: 48px; width: 44px; height: 44px;
    border-radius: 50%; background: var(--brand-blue);
  }

  .who-ribbon { position: absolute; left: 14px; top: 486px; width: 349px; height: 600px; }
  .who-ribbon svg { position: absolute; inset: 0; }
  .who-content { position: absolute; left: 40px; top: 0; width: 300px; color: #fff; }
  .who-title {
    margin-top: 60px; text-align: center; color: var(--brand-green);
    font-weight: 700; font-size: 19px; letter-spacing: .5px;
  }
  .who-content p { font-size: 18.5px; line-height: 24px; text-align: justify; margin-top: 24px; }

  .contact { position: absolute; left: 29px; width: 334px; top: 1094px; text-align: center; }
  .contact li { list-style: none; color: var(--brand-blue); font-weight: 700; font-size: 18px; line-height: 28px; }

  .statement { position: absolute; left: 392px; width: 574px; }
  .statement h2 {
    display: flex; align-items: center; gap: 8px;
    font-size: 20px; font-weight: 400; color: var(--brand-blue); margin-bottom: 4px;
  }
  .statement h2 strong { font-weight: 700; }
  .statement h2 .bullet {
    width: 20px; height: 20px; border-radius: 50%; border: 3px solid var(--brand-blue); flex: none;
  }
  .statement p { font-size: 18.3px; line-height: 23.5px; text-align: justify; }
  .vision { top: 544px; }
  .mission { top: 838px; }
  .values { top: 990px; }

  .footer-band { position: absolute; left: 0; bottom: 0; width: 1005px; height: 12px; background: var(--brand-green); }
</style>
</head>
<body>
<main class="poster">
  <header class="header-bar">
    <h1 class="header-title">BRAND STANDARDS &amp; CORE VALUES</h1>
  </header>

  <div class="hero-photo" role="img" aria-label="Photo of a smiling senior woman in a wheelchair outdoors with a caregiver in blue scrubs beside her, trees in the background"></div>

  <div class="logo-panel">
    <svg width="334" height="230" viewBox="0 0 334 230"><polygon points="0,0 334,0 334,198 167,228 0,198" fill="#FFFFFF"/></svg>
    <span class="logo-dot"></span>
    <div class="logo-mark">CareWillow</div>
  </div>

  <aside class="who-ribbon">
    <svg width="349" height="600" viewBox="0 0 349 600">
      <polygon points="0,16 15,0 15,16" fill="var(--ribbon-fold)"/>
      <polygon points="15,0 349,0 349,600 182,568 15,600" fill="var(--ribbon-blue)"/>
    </svg>
    <div class="who-content">
      <h2 class="who-title">WHO WE ARE:</h2>
      <p>We are friendly, servant leaders who have a sense of urgency to meet the needs of our nurses and clients.</p>
      <p>We prioritize personal relationships with genuine caring and compassion. We inspire others through our passion and energy.</p>
      <p>We are caregivers, sevant leaders, and difference-makers who never forget why we are here: to serve.</p>
      <p>We are ansewering the call to care</p>
    </div>
  </aside>

  <ul class="contact">
    <li>555-010-4427</li>
    <li>office@carewillow.example</li>
    <li>www.carewillow.example</li>
  </ul>

  <section class="statement vision">
    <h2><span class="bullet"></span><span><strong>OUR VISION</strong> STATEMENT:</span></h2>
    <p>We are transforming the healthcare staffing and home-care industry with our people-oriented, world-class team. Clients choose us, and develop lasting bonds with our team because of our impeccably high standards and our reputation for always remembering this is, first and foremost, a people business. We consistently go the extra mile to ensure our nurses and those being cared for are at all times, treated with dignity and respect. We hold ourselves and those we work with to the highest possible standards. We consistently deliver what we promise, and whenever possible, even more.</p>
  </section>

  <section class="statement mission">
    <h2><span class="bullet"></span><span><strong>OUR MISSION</strong> STATEMENT:</span></h2>
    <p>We go above and beyond to ensure our clients receive the right care and the right people at the right time. Our rigorous recruitment standards result in strong caregivers who are trusted for their expertise, experience and compassion.</p>
  </section>

  <section class="statement values">
    <h2><span class="bullet"></span><span><strong>OUR</strong> VALUES:</span></h2>
    <p>Through our genuine caring and compassion, we are committed to honor all with whom we interact. We are grounded in our faith and dedicated to working together as a family that consistently and passionately lives our values. Compassion Integrity and honesty Faith Decisive action Constant and never-ending improvement Personal ownership Excellence Positive attitude Passion Respect</p>
  </section>

  <div class="footer-band"></div>
</main>
</body>
</html>
```